Redesign two existing website pages and one new landing page for dental office

I need to redesign two webpages on my dental website, the Home page (http://brelvoortdental.com) and the Dental Implant Services page (http://www.brelvoortdental.com/dental-implant-services) and also create a landing page for the Dental Implant Services page.

Please use the same color scheme, slogans and subtitles for the redesign pages and create a reserved video spot on each page. The video spots should not be too big but not too small either and positioned in a central key location on each of the pages. The final redesigned pages should communicate leadership, confidence and trust.

The new landing page for the Dental implant Services page must not have any hyperlinks on the page and must entice the viewer to give name and email before downloading a "Free" eBook called "Is a Fresh Smile Worth Waiting For?" Any added photo images to this new page must be smiling.
Updates

Project Deadline Extended Reason: I got feedback that my project was not long enough so I'm extending it by 5 days. Added Thursday, April 16, 2015

Target Market(s)

People who are middle-age to seniors.

Industry/Entity Type

Dental

Coding

Coded - Design and coding required

Number of Pages Required

3 page

Requirements
Must have
• Compatible with existing website colors and theme.

```html
<!DOCTYPE html>
<html lang="en">
<head>
<meta charset="utf-8">
<title>Brelvoort Dental Care – Home</title>
<link rel="stylesheet" href="https://fonts.googleapis.com/css2?family=Arimo:wght@400;700&display=swap">
<style>
:root{
  --stage:#7f7f7f;
  --paper:#ffffff;
  --brown:#8b7b6d;
  --teal:#6fab9b;
  --green:#3f6b5c;
  --green-mid:#4f7a6c;
  --band:#e0eae6;
  --ink:#333333;
  --link:#5e9e8c;
}
*{margin:0;padding:0;box-sizing:border-box}
html,body{width:1200px;height:1000px;overflow:hidden;background:var(--stage);font-family:Arimo,Arial,sans-serif;color:var(--ink)}
.page{position:absolute;left:337px;top:27px;width:565px;height:948px;background:var(--paper)}
.abs{position:absolute}
.brand{left:86px;top:12px;width:122px;font-size:10.5px;color:var(--teal);white-space:nowrap;overflow:hidden}
.brand .sq{display:inline-block;width:7px;height:7px;background:var(--teal);margin-right:3px}
.quick{top:8px;display:flex;align-items:center;gap:5px;font-size:5.5px;line-height:1.35;color:var(--green);white-space:nowrap}
.quick svg{width:14px;height:20px;flex:none}
.nav{left:91px;top:41px;display:flex;font-size:6.5px;color:var(--green);white-space:nowrap}
.nav span{margin-right:13px}
.social{top:40px;display:flex;gap:2px}
.social i{display:block;width:7px;height:7px;background:var(--brown)}
.photo{background:linear-gradient(180deg,#dce8ef 0%,#e9eef0 55%,#c9b7a3 80%,#7d9a3e 96%)}
.headline{left:0;width:565px;top:200px;text-align:center;font-size:15.5px;font-weight:700;color:var(--brown)}
.headline em{font-style:normal;color:var(--teal)}
.band{left:0;top:235px;width:565px;height:149px;background:var(--band);border-top:1px solid var(--green);border-bottom:1px solid var(--green)}
.band .divider{left:276px;top:0;width:1px;height:148px;background:var(--green)}
.svc h2{font-size:11.5px;color:var(--brown)}
.svc h3{font-size:9px;color:var(--green);margin-top:5px}
.svc .thumb{width:79px;height:53px;margin-top:4px}
.svc .desc{left:86px;top:43px;width:108px;font-size:5.3px;line-height:1.4}
.btn{display:inline-block;background:var(--green);color:#fff;font-size:5.2px;padding:3px 6px;border:1px solid #2c4d42}
.svc .rem{font-size:5.4px;font-weight:700;margin-top:5px}
.svc ul{font-size:5.2px;line-height:1.45;margin:4px 0 0 16px}
.video{left:106px;top:400px;width:353px;height:188px;background:linear-gradient(90deg,#5b3a22 0%,#3a2416 45%,#6a4530 100%)}
.play{left:160px;top:82px;width:33px;height:22px;background:#111;border-radius:5px;opacity:.85}
.play:after{content:"";position:absolute;left:13px;top:6px;border-left:9px solid #fff;border-top:5px solid transparent;border-bottom:5px solid transparent}
.col h4{font-size:12px;color:var(--green-mid);line-height:1.05}
.col ul{font-size:5.3px;line-height:1.6;margin:4px 0 0 8px}
.cta{left:78px;top:771px;width:410px;height:18px;background:var(--green-mid);border:1px solid #9fb8ae;color:#e8f0ec;font-size:6.5px;text-align:center;line-height:16px}
.foot h5{font-size:12px;color:var(--brown)}
.foot p,.foot li{font-size:5.4px;line-height:1.45}
.foot a{color:var(--link);text-decoration:none}
.foot ul{margin:6px 0 0 8px}
.footer{left:0;top:919px;width:565px;height:29px;background:var(--green);color:#fff;font-size:4.6px}
.footer .social i{background:#fff}
.footer .addr{left:88px;top:17px;width:225px;white-space:nowrap;overflow:hidden}
</style>
</head>
<body>
<div class="page">
  <div class="abs brand"><span class="sq"></span>Brelvoort Dental Care</div>
  <div class="abs quick" style="left:216px"><svg viewBox="0 0 14 20"><rect x="1" y="1" width="12" height="18" rx="1" fill="var(--green)"/><rect x="3" y="3" width="8" height="12" fill="#fff"/></svg><span>Get Dr. Brelvoort's<br>Mobile App</span></div>
  <div class="abs quick" style="left:289px"><svg viewBox="0 0 14 20"><rect x="1" y="4" width="13" height="13" fill="var(--green)"/><path d="M3 8h9M3 11h9M3 14h9" stroke="#fff" stroke-width="1"/></svg><span>Request an<br>Appointment</span></div>
  <div class="abs quick" style="left:360px"><svg viewBox="0 0 14 20"><rect x="1" y="1" width="12" height="18" fill="var(--green)"/><path d="M3 6h8M3 9h8M3 12h8M3 15h6" stroke="#fff" stroke-width="1"/></svg><span>New Patient<br>Online Forms</span></div>
  <div class="abs quick" style="left:430px"><svg viewBox="0 0 14 20"><rect x="2" y="1" width="10" height="18" rx="1" fill="var(--green)"/><rect x="4" y="3" width="6" height="4" fill="#fff"/><path d="M4 10h2M8 10h2M4 13h2M8 13h2M4 16h2M8 16h2" stroke="#fff"/></svg><span>Call Us Today!<br>(281) 555-0147</span></div>
  <nav class="abs nav"><span>HOME</span><span>ABOUT US</span><span>DENTAL SERVICES</span><span>BLOG</span><span>CONTACT US</span><span>TESTIMONIALS</span></nav>
  <div class="abs social" style="left:436px"><i></i><i></i><i></i><i></i><i></i></div>

  <div class="abs photo" style="left:79px;top:56px;width:409px;height:126px" role="img" aria-label="Photo of a smiling multi-generation family sitting together on grass"></div>

  <h1 class="abs headline">Life-Changing <em>Family Dental Care</em> In Sugar Land</h1>

  <section class="abs band">
    <div class="abs divider"></div>
    <div class="abs svc" style="left:78px;top:9px;width:190px">
      <h2>Dental Hygiene Services</h2>
      <h3>Achieve Better Health With Prevention</h3>
      <div class="thumb" style="background:linear-gradient(135deg,#f4f6f7,#cfe3e9)" role="img" aria-label="Photo of a toothbrush and dental floss"></div>
      <div class="abs desc">Maintain healthy teeth and gums with consistent dental exams and teeth cleanings by one of our professional dental hygienists.<br><span class="btn" style="margin-top:8px">Learn More</span></div>
      <p class="rem">Remember:</p>
      <ul><li>Improve your health with consistent dental checkups</li><li>Save time with convenient appointment options close to home</li><li>Teach kids to develop good dental habits and to maintain a life time of preventive dental care</li></ul>
    </div>
    <div class="abs svc" style="left:288px;top:9px;width:200px">
      <h2>Dental Emergency Services</h2>
      <h3>Stop Pain From Tooth Trauma and Infection</h3>
      <div class="thumb" style="background:linear-gradient(135deg,#8dbb4a,#f1d8c8)" role="img" aria-label="Photo of a person biting a green apple"></div>
      <div class="abs desc">Dental emergencies can and will happen suddenly. Treat all tooth infections and dental trauma (without delay) whenever they occur.<br><span class="btn" style="margin-top:8px">Learn More</span></div>
      <p class="rem">Remember:</p>
      <ul><li>Repair your broken, fractured, or lost teeth</li><li>Call our dental office to reach our <a style="color:var(--link)">Sugar Land dentist</a> for an immediate response to avoid further tooth damage and infection</li><li>Overcome dental anxiety with comforting dental sedation</li></ul>
    </div>
  </section>

  <div class="abs video" role="img" aria-label="Welcome video from the dentist in his office"><div class="abs play"></div></div>

  <div class="abs col" style="left:79px;top:625px;width:95px">
    <div style="width:95px;height:62px;background:linear-gradient(180deg,#f5d6d3,#e88b8b)" role="img" aria-label="Photo of a set of dentures"></div>
    <h4 style="margin-top:7px;margin-left:4px">Beautiful<br>Dentures</h4>
    <ul style="margin-left:-2px"><li>What is a Denture?</li><li>Who Needs a Denture?</li><li>Just How Are Dentures Made?</li></ul>
  </div>
  <div class="abs col" style="left:186px;top:625px;width:93px">
    <div style="width:93px;height:40px;background:linear-gradient(180deg,#c98774,#f3ede6 50%,#c98774)" role="img" aria-label="Close-up photo of a white smile"></div>
    <h4 style="margin-top:8px">Cosmetic<br>Dentistry</h4>
    <ul><li>Whiten Your Teeth</li><li>Porcelain Veneers</li><li>Clear Aligner Therapy Orthodontics</li></ul>
  </div>
  <div class="abs col" style="left:287px;top:622px;width:93px">
    <div style="width:93px;height:38px;background:linear-gradient(180deg,#f3f3f3,#eccbc9)" role="img" aria-label="Illustration of a dental implant in the jaw"></div>
    <h4 style="margin-top:8px">Dental Implant<br>Services</h4>
    <ul><li>Anchorage to the jaw bone</li><li>Replaces 1 or more missing teeth</li><li>Stabilizes loose, floppy dentures</li></ul>
  </div>
  <div class="abs col" style="left:390px;top:622px;width:93px">
    <div style="width:93px;height:55px;background:linear-gradient(135deg,#dfe8ee,#6f8ea6)" role="img" aria-label="Photo of a dentist reviewing an x-ray with a patient"></div>
    <h4 style="margin-top:12px">Sedation<br>Dentistry</h4>
    <ul><li>Control Dental Fear with Sedation Dentistry</li><li>Dental Pain Management</li><li>Relaxed and Tranquil Treatment</li></ul>
  </div>

  <div class="abs cta">Comprehensive Family Dentistry in One Sugar Land Dental Office! Schedule An Appointment?</div>

  <div class="abs foot" style="left:78px;top:810px;width:130px">
    <h5>Don't Wait 'til it Hurts!</h5>
    <div class="abs" style="left:0;top:25px;width:58px;height:59px;background:linear-gradient(135deg,#f1e4dc,#d9bfae)" role="img" aria-label="Photo of a person holding their cheek with tooth pain"></div>
    <div class="abs" style="left:62px;top:26px;width:68px">
      <p><a>Get acquainted today with comfortable dental care.</a></p>
      <p style="margin-top:12px"><a>Request an Appointment</a><br>We will contact you right away to schedule your dental appointment.</p>
    </div>
  </div>
  <div class="abs foot" style="left:217px;top:810px;width:130px">
    <h5>Recent Blog Posts</h5>
    <ul style="margin-top:4px"><li><a>Conscious Sedation: A Way to Deal with Anxiety at the Dentist's Office</a></li><li><a>Pediatric Dentists and Their Importance in Today's World</a></li><li><a>Tooth Implant Facts</a></li><li><a>Is Sedation Dentistry Cost Affordable?</a></li><li><a>How to Prepare for Oral Surgery</a></li></ul>
  </div>
  <div class="abs foot" style="left:358px;top:810px;width:128px">
    <h5>Contact Us...</h5>
    <p style="margin-top:4px">for all your general and cosmetic dental treatment and ask how to eliminate your dental pain and anxiety with <a>sedation dentistry</a>.</p>
    <p style="margin-top:5px;margin-left:18px"><a>Email Us</a>&nbsp;&nbsp;&nbsp;&nbsp;&nbsp;&nbsp; Phone &nbsp;(281) 555-0147</p>
    <div style="width:125px;height:45px;margin-top:3px;background:linear-gradient(180deg,#6e9fd6 0%,#b8cfe6 45%,#c9c3b8 70%,#8d8f86 100%)" role="img" aria-label="Photo of the medical center building"></div>
    <p style="text-align:center"><a>Directions to the Lakeside Medical Center</a></p>
  </div>

  <footer class="abs footer">
    <div class="abs social" style="left:435px;top:2px"><i style="width:9px;height:9px"></i><i style="width:9px;height:9px"></i><i style="width:9px;height:9px"></i><i style="width:9px;height:9px"></i><i style="width:9px;height:9px"></i></div>
    <span class="abs addr">©2014 Brelvoort Dental Care, Lakeside Medical Ctr, 2450 Orchard Pkwy, Ste. #140, Sugar Land, TX 77479</span>
    <span class="abs" style="left:322px;top:17px;font-size:5.5px">Se Habla Español</span>
    <span class="abs" style="left:450px;top:17px;font-size:5.5px">(281) 555-0147</span>
  </footer>
</div>
</body>
</html>
```